Roll Up Banner for Lifestyle / medical company

I need a roll-up banner for a congress highlighting our lifestyle company that aids people with diabetes type 2 through diet and exercise. The banner should capture our unique approach and appeal to medical professionals.

120x200 cm

Scope of work
- Design a roll-up banner for a congress.
- Include the programme name: Koers Suikerwijzer Route.
- Add the catchphrase: Het individuele leefstijlprogramma voor 50-plussers met diabetes type 2.
- Feature the 4 pillars: Digitaal en persoonlijk, Duurzame begeleiding, Bewezen resultaten, Aanvulling ketenzorg.

References
- See our style at groenbordvitaal.nl and in the files attached

Additional information
The banner should appeal to medical professionals attending the congress.

Company details
- Company website: groenbordvitaal.nl
- We are a lifestyle company dedicated to helping people manage diabetes type 2 through tailored diet and exercise programs. Our target audience for this banner is medical professionals.

We can provide photo's of older individuals in our style. Contact us at info@groenbordvitaal.nl for these pictures.

```html
<!DOCTYPE html>
<html lang="nl">
<head>
<meta charset="utf-8">
<title>Koers Suikerwijzer Route – roll-up banner</title>
<link rel="stylesheet" href="https://fonts.googleapis.com/css2?family=Figtree:wght@400;600;700;800&display=swap">
<style>
  :root {
    --page: #eef1f0;
    --mint: #dcefe0;
    --forest: #134c39;
    --teal: #3b9886;
    --ink: #0f3a2c;
    --white: #ffffff;
    --photo-light: #e9d3b0;
    --photo-warm: #e2ab5f;
  }
  * { box-sizing: border-box; margin: 0; padding: 0; }
  html, body {
    width: 1200px; height: 908px; overflow: hidden;
    background: var(--page);
    font-family: "Figtree", "Helvetica Neue", Arial, sans-serif;
  }
  .banner {
    position: absolute; left: 400px; top: 9px;
    width: 400px; height: 890px;
    background: var(--mint);
    overflow: hidden;
  }
  .brand {
    position: absolute; left: 26px; top: 100px;
    display: flex; align-items: center; gap: 10px;
  }
  .brand-square { width: 24px; height: 24px; background: var(--forest); }
  .brand-name { font-weight: 800; font-size: 22px; color: var(--forest); letter-spacing: -0.2px; }
  .title {
    position: absolute; left: 26px; top: 192px; width: 340px;
    font-weight: 800; font-size: 39px; line-height: 1.03;
    color: var(--forest); letter-spacing: -0.5px;
  }
  .photo {
    position: absolute; left: 226px; top: 262px; width: 174px; height: 264px;
    background: linear-gradient(180deg, var(--mint) 0%, var(--photo-light) 35%, var(--photo-warm) 100%);
  }
  .tagline {
    position: absolute; left: 26px; top: 362px; width: 195px;
    font-weight: 700; font-size: 18px; line-height: 1.2; color: var(--ink);
  }
  .pillars { position: absolute; left: 0; top: 526px; width: 100%; list-style: none; }
  .pillar {
    height: 64px; margin-bottom: 7px;
    display: flex; align-items: center; gap: 22px; padding-left: 26px;
    color: var(--white); font-weight: 700; font-size: 22px; white-space: nowrap;
  }
  .pillar:nth-child(odd) { background: var(--forest); }
  .pillar:nth-child(even) { background: var(--teal); }
  .pillar svg { width: 44px; height: 44px; flex: none; }
  .contact {
    position: absolute; left: 0; top: 834px; width: 100%;
    text-align: center; color: var(--ink);
  }
  .contact .email { font-weight: 400; font-size: 25px; line-height: 1.15; }
  .contact .site { font-weight: 800; font-size: 25px; line-height: 1.15; }
</style>
</head>
<body>
  <main class="banner">
    <div class="brand">
      <span class="brand-square"></span>
      <span class="brand-name">Groenbord Vitaal</span>
    </div>

    <h1 class="title">Koers Suikerwijzer Route</h1>

    <div class="photo" role="img" aria-label="Foto van een lachende oudere vrouw in een oranje shirt met gekruiste armen"></div>

    <p class="tagline">Het individuele<br>leefstijlprogramma<br>voor 50-plussers<br>met diabetes<br>type 2</p>

    <ul class="pillars">
      <li class="pillar">
        <svg viewBox="0 0 40 40" fill="none" stroke="#fff" stroke-width="1.8" stroke-linecap="round">
          <rect x="13" y="3" width="16" height="32" rx="3"/>
          <circle cx="21" cy="12" r="3.5"/>
          <path d="M16 21h10M16 25h10M16 29h6"/>
          <path d="M13 20c-4 2-6 6-5 11l3 6"/>
        </svg>
        Digitaal en persoonlijk:
      </li>
      <li class="pillar">
        <svg viewBox="0 0 40 40" fill="none" stroke="#fff" stroke-width="1.8" stroke-linecap="round">
          <circle cx="13" cy="9" r="4"/><circle cx="27" cy="11" r="3.5"/>
          <path d="M5 24c0-5 4-8 8-8s8 3 8 8M21 24c0-4 3-7 6-7s7 3 7 7"/>
          <path d="M3 30c6 0 9 3 15 3s11-3 17-6"/>
        </svg>
        Duurzame begeleiding:
      </li>
      <li class="pillar">
        <svg viewBox="0 0 40 40" fill="none" stroke="#fff" stroke-width="1.8" stroke-linecap="round">
          <path d="M4 3v33h33"/>
          <rect x="9" y="26" width="5" height="10"/><rect x="17" y="22" width="5" height="14"/>
          <rect x="25" y="18" width="5" height="18"/>
          <path d="M8 20l9-7 6 4 11-10M28 7h6v6"/>
        </svg>
        Bewezen resultaten:
      </li>
      <li class="pillar">
        <svg viewBox="0 0 40 40" fill="none" stroke="#fff" stroke-width="1.8" stroke-linecap="round">
          <rect x="4" y="17" width="20" height="11" rx="5.5" transform="rotate(-45 14 22)"/>
          <rect x="16" y="12" width="20" height="11" rx="5.5" transform="rotate(-45 26 17)"/>
        </svg>
        Aanvulling ketenzorg:
      </li>
    </ul>

    <div class="contact">
      <p class="email">info@groenbordvitaal.nl</p>
      <p class="site">groenbordvitaal.nl</p>
    </div>
  </main>
</body>
</html>
```